RM Kargovo businesscard project

RM Cargoline Ltd is a freshly founded small (3 employees), young (average age is 30 years) company, living from the road transportation market without own tools.
We would like to have an impressive, new-line, cool busines card for a freshly founded forwarding company on an overcrowded market which raises attention and makes the potential partners eager to work with us.

Target Market(s)

The main profile of the company is logistic/forwarding on road.

Industry/Entity Type

Freight Forwarding

Contact Information for Business Card

Name: Berki Zsófia
Title: general manager
mobile nr: +36-70/555-0142
fax nr: +36-1/555-0187
e-mail: zsofia.berki@rmkargovo.example
info@rmkargovo.example
website address: http://www.rmcargoline.example
and if possible maybe some funny or helpful info on the back

Requirements
Must have
• contact details above
Nice to have
• some really nice and catching back-side (info, graphics, useful tool info... anything)
Should not have
• trucks, road, ship, airplane on it...

```html
<!DOCTYPE html>
<html lang="hu">
<head>
<meta charset="utf-8">
<title>RM Kargovo – Business Card</title>
<link href="https://fonts.googleapis.com/css2?family=Lato:wght@400;700;900&display=swap" rel="stylesheet">
<style>
  :root {
    --navy: #0c0c5a;
    --white: #ffffff;
    --backdrop: #e9e6e1;
    --card-edge: #1a1a1a;
  }
  * { margin: 0; padding: 0; box-sizing: border-box; }
  html, body {
    width: 1200px; height: 900px; overflow: hidden;
    background: var(--backdrop);
    font-family: "Lato", Arial, sans-serif;
  }
  .stage { position: relative; width: 1200px; height: 900px; }

  .card {
    position: absolute;
    width: 560px; height: 320px;
    background: var(--white);
    overflow: hidden;
    box-shadow: 4px 6px 0 var(--card-edge), 0 10px 24px rgba(0,0,0,.18);
  }
  .card--front { left: 50px; top: 100px; }
  .card--back  { left: 590px; top: 470px; }

  .band {
    position: absolute; left: 0; right: 0;
    background: var(--navy);
  }
  .card--front .band { top: 110px; height: 182px; }
  .card--back  .band { top: 78px; height: 170px; }

  .brand {
    position: absolute;
    display: flex; align-items: center; gap: 12px;
    font-weight: 900; white-space: nowrap;
  }
  .brand__mark { width: 30px; height: 30px; flex: none; }
  .card--front .brand { left: 160px; top: 36px; font-size: 32px; color: var(--navy); }
  .card--front .brand__mark { background: var(--navy); }
  .card--back .brand {
    right: 40px; top: 112px; font-size: 32px; color: var(--white);
    flex-direction: column; align-items: flex-end; gap: 12px;
  }
  .card--back .brand__mark { background: var(--white); width: 40px; height: 40px; }

  .person {
    position: absolute; right: 34px; top: 26px;
    color: var(--white); line-height: 1; white-space: nowrap;
  }
  .person__name { font-size: 26px; letter-spacing: .5px; text-transform: uppercase; }
  .person__name b { font-weight: 900; }
  .person__name span { font-weight: 400; }
  .person__title { font-size: 13px; margin-top: 4px; text-align: right; }

  .contacts {
    position: absolute; left: 36px; top: 64px;
    list-style: none; color: var(--white);
    font-size: 15px; line-height: 1.35; white-space: nowrap;
  }
  .contacts li { display: flex; align-items: flex-start; gap: 12px; }
  .contacts .icon { width: 13px; height: 13px; margin-top: 4px; flex: none; fill: var(--white); }
  .contacts .spacer { width: 13px; flex: none; }
  .contacts li.web { margin-top: 8px; }

  .web-line {
    position: absolute; right: 40px; bottom: 22px;
    display: flex; align-items: center; gap: 12px;
    color: var(--navy); font-size: 18px;
  }
  .web-line .icon { width: 16px; height: 16px; fill: var(--navy); }
</style>
</head>
<body>
<div class="stage">

  <section class="card card--front" aria-label="Business card front">
    <div class="brand"><span class="brand__mark"></span>RM Kargovo</div>
    <div class="band">
      <div class="person">
        <div class="person__name"><b>Berki</b> <span>Zsófia</span></div>
        <div class="person__title">General Manager</div>
      </div>
      <ul class="contacts">
        <li>
          <svg class="icon" viewBox="0 0 16 16"><path d="M2 5c0-2 3-3 6-3s6 1 6 3v1h-3V5H5v1H2zM4 7h8l2 6H2z"/></svg>
          +36-70/555-0142
        </li>
        <li>
          <svg class="icon" viewBox="0 0 16 16"><path d="M4 1h8v4H4zM1 6h14v6h-3v3H4v-3H1zM5 10v4h6v-4z"/></svg>
          +36-1/555-0187
        </li>
        <li>
          <svg class="icon" viewBox="0 0 16 16"><path d="M1 3h14v10H1zM2.5 4.5 8 9l5.5-4.5v-.5h-11z" fill-rule="evenodd"/></svg>
          zsofia.berki@rmkargovo.example
        </li>
        <li><span class="spacer"></span>info@rmkargovo.example</li>
        <li class="web">
          <svg class="icon" viewBox="0 0 16 16"><circle cx="8" cy="8" r="7"/><path d="M1 8h14M8 1c-3 3-3 11 0 14M8 1c3 3 3 11 0 14" stroke="#0c0c5a" stroke-width="1" fill="none"/></svg>
          www.rmkargovo.example
        </li>
      </ul>
    </div>
  </section>

  <section class="card card--back" aria-label="Business card back">
    <div class="band"></div>
    <div class="brand"><span class="brand__mark"></span>RM Kargovo</div>
    <div class="web-line">
      <svg class="icon" viewBox="0 0 16 16"><circle cx="8" cy="8" r="7"/><path d="M1 8h14M8 1c-3 3-3 11 0 14M8 1c3 3 3 11 0 14" stroke="#ffffff" stroke-width="1" fill="none"/></svg>
      www.rmkargovo.example
    </div>
  </section>

</div>
</body>
</html>
```